Coldforge Prime manufacturing Project

We are looking at getting a brand new design for a new company that deals in selling stainless tubing and other stainless still products such as handrails, Spigots, Balustrade Fittings
Glass, Glass fittings and Aluminium Channels

We require a very clean website that deals with the following colours:

Blue to light blues
Blacks
Greys to light Greys
Whites

We are open for other ideas BUT we *DO NOT* want any pinks, greens or bright colours except for backgrounds colours we have chosen above. (It can be solid, gradient or a subtle pattern)

YOU MUST KEEP THE LOGO AS IS. PLEASE DO NOT ALTER THE LOGO IN *ANY WAY* and the logo MUST be the same colours and fonts.

Logo is attached.

The site must contain these aspects:
jQuery Slider (Image slide show)
Top drop down Menus
Be no more than 900px wide
Text is to be to the w3C standards. (no special fonts)

We will chop up the design into html format. You just need to provide the PSD file.

The clients opposition is:
www.quorvatrim.example

Industry/Entity Type

It Company

Requirements
Nice to have
• Alter the logo in anyway

Files

```html
<!DOCTYPE html>
<html lang="en">
<head>
<meta charset="utf-8">
<title>Coldforge Prime Manufacturing</title>
<link href="https://fonts.googleapis.com/css2?family=Open+Sans:ital,wght@0,300;0,400;0,600;0,700;1,400&display=swap" rel="stylesheet">
<style>
:root{
  --page:#eeeeee;
  --ink:#1b1b1b;
  --text:#444444;
  --blue:#2f5a8c;
  --blue-btn:#3e6aa1;
  --rule:#d6d6d6;
  --dark-btn:#3a3a3a;
  --footer:#252525;
  --footer-text:#c9c9c9;
  --footer-bottom:#1c1c1c;
  --white:#ffffff;
}
*{margin:0;padding:0;box-sizing:border-box}
html,body{width:953px;height:1200px;overflow:hidden}
body{background:var(--page);font-family:'Open Sans',Arial,sans-serif;color:var(--text);position:relative}
.abs{position:absolute}

/* header */
.brand-mark{left:104px;top:8px;width:82px;height:82px;border-radius:50%;background:#2a2a2a;border:4px solid #9fb4cc}
.brand-name{left:66px;top:98px;width:160px;text-align:center;font-size:17px;font-weight:400;color:#333;line-height:1.1}
.brand-sub{left:66px;top:119px;width:160px;text-align:center;font-size:8px;font-weight:400;color:#333;letter-spacing:1.6px}
.search{left:356px;top:40px;width:342px;height:30px;background:var(--white);border:1px solid #d4d4d4;font-size:10px;font-style:italic;color:#777;padding:8px 9px}
.search svg{position:absolute;right:8px;top:7px}
.call{left:710px;top:44px;font-size:17px;color:#444;font-weight:400}
.call b{color:var(--blue);font-weight:600;font-size:20px}
.nav{left:356px;top:104px;display:flex;height:34px}
.nav a{display:block;padding:0 14px;line-height:34px;font-size:12.5px;font-weight:600;color:#333;text-decoration:none}
.nav a.current{background:var(--blue-btn);color:var(--white);padding:0 15px}

/* media areas */
.media{border:1px solid #d8d8d8;box-shadow:inset 0 0 0 1px rgba(255,255,255,.35)}
.slider{left:72px;top:153px;width:798px;height:331px;
  background:
    radial-gradient(ellipse at 30% 35%,rgba(255,255,255,.75),rgba(255,255,255,0) 45%),
    radial-gradient(ellipse at 75% 70%,rgba(255,255,255,.6),rgba(255,255,255,0) 40%),
    linear-gradient(120deg,#9fb0d6 0%,#27366e 22%,#dfe6f5 40%,#4a5d99 58%,#f1f4fb 75%,#1f2b5c 90%,#b7c3e2 100%)}
.dots{left:452px;top:464px;display:flex;gap:4px}
.dots span{width:9px;height:9px;border-radius:50%;background:#b8c2d6}
.dots span.on{background:#23468a}

/* sections */
.heading{font-size:15.5px;font-weight:600;color:var(--blue);text-transform:uppercase}
.rule-dash{left:71px;width:800px;border-top:1px dashed #cfcfcf}
.rule{left:71px;width:800px;border-top:1px solid var(--rule)}
.product{width:190px}
.product .thumb{height:90px;width:188px}
.product h3{margin-top:14px;font-size:15.5px;font-weight:700;color:var(--ink);text-transform:uppercase;white-space:nowrap;line-height:20px}
.product p{margin-top:1px;font-size:10.2px;line-height:13.5px;color:#444;padding-left:1px;letter-spacing:-.15px}
.btn-dark{display:inline-block;margin-top:11px;margin-left:1px;background:var(--dark-btn);color:var(--white);font-size:11.5px;padding:3px 7px;border:1px solid #222;outline:1px solid #bbb;font-weight:300}
.welcome p{font-size:11px;line-height:17.5px;color:#444;margin-bottom:8px;font-weight:300;letter-spacing:-.1px}
.btn-blue{left:73px;top:920px;width:73px;height:23px;background:var(--blue-btn);color:var(--white);font-size:12px;text-align:center;line-height:22px;outline:1px solid #a9bbd3;font-weight:300}

/* footer */
.footer{left:0;top:969px;width:953px;height:187px;background:var(--footer);border-top:2px solid #111}
.footer h4{position:absolute;font-size:14px;font-weight:600;color:var(--white);text-transform:uppercase}
.footer p{font-size:11px;line-height:16.5px;color:var(--footer-text);font-weight:300}
.avatar{width:46px;height:46px;border:1px solid #444;background:radial-gradient(circle at 50% 40%,#d9b49a 0 35%,#8a6a58 60%,#efefef 61%)}
.gallery-item{width:82px;height:47px;border:1px solid #d0d0d0}
.bottom{left:0;top:1156px;width:953px;height:44px;background:var(--footer-bottom);border-top:1px solid #333}
.bottom-links{left:70px;top:1170px;display:flex;gap:24px;font-size:11px;color:#9a9a9a;font-weight:300}
.copyright{right:82px;top:1170px;font-size:11px;color:#9a9a9a;font-weight:300}
</style>
</head>
<body>

<header>
  <div class="abs brand-mark"></div>
  <div class="abs brand-name">Coldforge Prime</div>
  <div class="abs brand-sub">Manufacturing Co. Ltd</div>

  <div class="abs search">Enter search here
    <svg width="14" height="14" viewBox="0 0 14 14"><circle cx="6" cy="6" r="4.5" fill="none" stroke="#bbb" stroke-width="1.6"/><line x1="9.3" y1="9.3" x2="13" y2="13" stroke="#bbb" stroke-width="1.8"/></svg>
  </div>
  <div class="abs call">Call: <b>0800 317 902</b></div>

  <nav class="abs nav">
    <a class="current">HOME</a><a>ABOUT US</a><a>PRODUCTS</a><a>SERVICES</a><a>WHO WE ARE</a><a>CONTACT</a>
  </nav>
</header>

<div class="abs slider media" role="img" aria-label="Close-up of polished chrome tap spouts in a row"></div>
<div class="abs dots"><span class="on"></span><span></span><span></span><span></span></div>

<h2 class="abs heading" style="left:71px;top:508px">Coldforge Prime Products</h2>
<div class="abs rule-dash" style="top:542px"></div>

<div class="abs product" style="left:72px;top:557px">
  <div class="thumb media" role="img" aria-label="Stainless steel stair handrail" style="background:linear-gradient(110deg,#a88c66 0%,#d8d2c4 30%,#b9c9d8 55%,#8ea6bf 100%)"></div>
  <h3>Handrails</h3>
  <p>On sait depuis longtemps que travailler avec du texte lisible</p>
  <span class="btn-dark">View All</span>
</div>
<div class="abs product" style="left:275px;top:557px">
  <div class="thumb media" role="img" aria-label="Chrome glass spigot fitting" style="background:radial-gradient(ellipse at 55% 50%,#9aa3ad 0,#c6c6c6 35%,#e2e2e2 75%)"></div>
  <h3>Spigots</h3>
  <p>On sait depuis longtemps que travailler avec du texte lisible</p>
  <span class="btn-dark">View All</span>
</div>
<div class="abs product" style="left:479px;top:557px">
  <div class="thumb media" role="img" aria-label="Glass balustrade in a bright interior" style="background:linear-gradient(160deg,#eef1f3 0%,#b8c3c8 45%,#9aa3a4 65%,#8a6c55 100%)"></div>
  <h3>Balustrade Fittings</h3>
  <p>On sait depuis longtemps que travailler avec du texte lisible</p>
  <span class="btn-dark">View All</span>
</div>
<div class="abs product" style="left:682px;top:557px">
  <div class="thumb media" role="img" aria-label="Bent aluminium channel profiles" style="background:linear-gradient(160deg,#7f766b 0%,#b7b0a5 40%,#d2ccc2 60%,#6f6960 100%)"></div>
  <h3>Aluminium Channels</h3>
  <p>On sait depuis longtemps que travailler avec du texte lisible</p>
  <span class="btn-dark">View All</span>
</div>

<div class="abs rule" style="top:755px"></div>

<section class="welcome">
  <h2 class="abs heading" style="left:71px;top:777px">Welcome to Coldforge Prime</h2>
  <div class="abs" style="left:73px;top:810px;width:800px">
    <p>Le Lorem Ipsum est simplement du faux texte employé dans la composition et la mise en page avant impression. Le Lorem Ipsum est le faux texte standard de l'imprimerie depuis les années 1500, quand un peintre anonyme.</p>
    <p>Assembla ensemble des morceaux de texte pour réaliser un livre spécimen de polices de texte.Il n'a pas fait que survivre cinq siècles.mais s'est aussi adapté à la bureautique informatique, sans que son contenu n'en soit modifié. Il a été popularisé dans les années 1960 grâce à la vente de feuilles Letraset contenant des passages.</p>
  </div>
  <div class="abs btn-blue">Read More</div>
</section>

<footer class="abs footer">
  <h4 style="left:71px;top:26px">Testimonials</h4>
  <div class="abs avatar" style="left:71px;top:57px" role="img" aria-label="Customer portrait"></div>
  <p class="abs" style="left:129px;top:57px;width:180px">On sait depuis longtemps que travailler avec du texte lisible et contenant du.</p>
  <div class="abs avatar" style="left:71px;top:120px" role="img" aria-label="Customer portrait"></div>
  <p class="abs" style="left:129px;top:120px;width:180px">On sait depuis longtemps que travailler avec du texte lisible et contenant du.</p>

  <h4 style="left:328px;top:26px">About Us</h4>
  <p class="abs" style="left:328px;top:57px;width:245px">On sait depuis longtemps que travailler avec du texte lisible et contenant du. sens est source de distractions.</p>
  <p class="abs" style="left:328px;top:123px;width:245px">On sait depuis longtemps que travailler avec du texte lisible et contenant du. sens est source de distractions, et empêche de se concentrer.</p>

  <h4 style="left:604px;top:26px">Image Gallery</h4>
  <div class="abs gallery-item" style="left:604px;top:57px;background:linear-gradient(135deg,#5a5a5a,#d4d4d4 50%,#7a7a7a)" role="img" aria-label="Handrail bracket"></div>
  <div class="abs gallery-item" style="left:697px;top:57px;background:linear-gradient(160deg,#e6eaec,#a6b2b6 55%,#8a6c55)" role="img" aria-label="Glass balustrade interior"></div>
  <div class="abs gallery-item" style="left:790px;top:57px;background:linear-gradient(135deg,#eeecf3,#b6b4c6 60%,#e0dfe9)" role="img" aria-label="Glass clamps"></div>
  <div class="abs gallery-item" style="left:604px;top:120px;background:linear-gradient(135deg,#e2e2e2,#8fa0a6 50%,#c2c2c2)" role="img" aria-label="Spiral glass staircase"></div>
  <div class="abs gallery-item" style="left:697px;top:120px;background:linear-gradient(135deg,#e9f4f7,#7fb3c9 50%,#d4e8ef)" role="img" aria-label="Water flowing from a tap"></div>
  <div class="abs gallery-item" style="left:790px;top:120px;background:linear-gradient(135deg,#1f3142,#d3dbe2 55%,#6c7f90)" role="img" aria-label="Chrome basin mixer"></div>
</footer>

<div class="abs bottom"></div>
<div class="abs bottom-links"><span>Home</span><span>About Us</span><span>Products</span><span>Services</span><span>Who we are</span><span>Contact</span></div>
<div class="abs copyright">© Copyrights 2013 All rights Reserved</div>

</body>
</html>
```